Corvalent Growth Partners in need of a business card design

We need an innovative business card designed for a new company in Alberta, Canada. We assist organizations in improving performance by providing coaching and mentorship on how to promote and achieve organizational excellence. We teach senior leaders and their staff on how to continually improve performance; assist them in making sure the organization is innovative, competitive, and customer focused; support them in making sure the culture of the organization is also healthy, inclusive, and sustainable; and they are economically, socially, and environmentally responsible. We will do this by staying true to our company values of respect, excellence, integrity and trust.

Attached is our newly designed logo.

The team thought that having an inspirational quote similar to this one below would be a good addition somewhere on the card.

"Autograph your work with excellence.''

Target Market(s)

Private and public sector organizations. Once that are interested in being a Top 100 employer.

Industry/Entity Type

Business

Font styles to use
Sans Serif

Requirements
Must have
• 1. The business card must be double-sided.
2. Person's name and title
3. Email address
4. Phone number
5. Website (corvalentgrowth.ca)
6. QR code
7. A quote somewhere on the front of the card: Autograph your work with excellence.
Nice to have

```html
<!DOCTYPE html>
<html lang="en">
<head>
<meta charset="utf-8">
<title>Corvalent Growth Partners – Business Card</title>
<link href="https://fonts.googleapis.com/css2?family=Nunito:wght@300;400;600;800&display=swap" rel="stylesheet">
<style>
  :root {
    --backdrop: #e9e9eb;
    --card: #ffffff;
    --ink: #111111;
    --ink-soft: #3a3a3a;
    --muted: #7d7d7d;
    --violet: #6a3d99;
    --violet-tint: #e6ddf1;
    --shadow: rgba(0, 0, 0, 0.12);
  }
  * { box-sizing: border-box; margin: 0; padding: 0; }
  html, body {
    width: 1200px;
    height: 800px;
    overflow: hidden;
    background: var(--backdrop);
    font-family: "Nunito", sans-serif;
  }
  .sheet {
    width: 1200px;
    height: 800px;
    display: flex;
    flex-direction: column;
    align-items: center;
    justify-content: center;
    gap: 60px;
  }
  .card {
    position: relative;
    width: 560px;
    height: 320px;
    background: var(--card);
    box-shadow: 0 6px 18px var(--shadow);
    overflow: hidden;
  }

  /* Front side */
  .card--front .brand {
    position: absolute;
    left: 84px;
    top: 70px;
    display: flex;
    align-items: center;
    gap: 22px;
  }
  .brand__mark {
    width: 58px;
    height: 58px;
    border-radius: 50%;
    background: var(--violet);
    flex: none;
  }
  .brand__name {
    font-weight: 800;
    font-size: 40px;
    line-height: 1.02;
    color: var(--ink);
    letter-spacing: -0.5px;
  }
  .card--front .quote {
    position: absolute;
    left: 0;
    right: 0;
    bottom: 52px;
    text-align: center;
    font-weight: 600;
    font-size: 13px;
    line-height: 1.65;
    color: var(--ink);
  }

  /* Back side */
  .card--back .accent {
    position: absolute;
    left: 170px;
    top: -60px;
    width: 440px;
    height: 440px;
    border-radius: 50%;
    background: var(--violet-tint);
    opacity: 0.55;
  }
  .card--back .person {
    position: absolute;
    left: 60px;
    top: 64px;
  }
  .person__name {
    font-weight: 800;
    font-size: 32px;
    line-height: 1.1;
    color: var(--ink);
  }
  .person__title {
    font-weight: 300;
    font-size: 20px;
    color: var(--muted);
    letter-spacing: 2px;
    margin-left: 62px;
  }
  .card--back .contact {
    position: absolute;
    right: 52px;
    bottom: 56px;
    list-style: none;
    font-weight: 300;
    font-size: 18px;
    line-height: 1.7;
    color: var(--ink-soft);
  }
</style>
</head>
<body>
  <main class="sheet">
    <section class="card card--front" aria-label="Card front">
      <div class="brand">
        <span class="brand__mark" aria-hidden="true"></span>
        <h1 class="brand__name">Corvalent<br>Growth Partners</h1>
      </div>
      <p class="quote">Every job is a self-portrait of the person who did it.<br>Autograph your work with excellence.</p>
    </section>

    <section class="card card--back" aria-label="Card back">
      <span class="accent" aria-hidden="true"></span>
      <div class="person">
        <h2 class="person__name">Dana Whitfield</h2>
        <p class="person__title">C.E.O.</p>
      </div>
      <ul class="contact">
        <li>info@corvalentgrowth.ca</li>
        <li>+1 403 555 0142</li>
        <li>corvalentgrowth.ca</li>
      </ul>
    </section>
  </main>
</body>
</html>
```